Bramwick Drywall Business Card

Looking to update the imagery, colors and logo to a more current design and to reflect their specialty of "High End" residential home construction

```html
<!DOCTYPE html>
<html lang="en">
<head>
<meta charset="utf-8">
<title>Bramwick Drywall Business Card</title>
<link rel="stylesheet" href="https://fonts.googleapis.com/css2?family=Roboto:wght@400;700;900&family=Russo+One&display=swap">
<style>
  :root {
    --page-bg: #2a2a2a;
    --brand-blue: #0b5db3;
    --brand-blue-deep: #0a4d9c;
    --brand-blue-light: #1a8ad4;
    --ink: #222831;
    --link-blue: #1565c0;
    --card-white: #f3f4f5;
    --photo-light: #e6e4df;
    --photo-mid: #c9c6bf;
    --photo-wood: #8a6a4c;
  }
  * { box-sizing: border-box; margin: 0; padding: 0; }
  html, body { width: 1200px; height: 1138px; overflow: hidden; }
  body { background: var(--page-bg); position: relative; font-family: "Roboto", Arial, sans-serif; }

  .card {
    position: absolute;
    width: 622px;
    height: 375px;
    border-radius: 16px;
    overflow: hidden;
  }

  /* Front */
  .card-front {
    left: 274px; top: 186px;
    background: linear-gradient(160deg, var(--brand-blue-deep) 0%, var(--brand-blue) 55%, var(--brand-blue-light) 100%);
  }
  .front-wordmark {
    position: absolute;
    left: 0; right: 0; top: 48px;
    text-align: center;
    color: #ffffff;
    font-family: "Roboto", Arial, sans-serif;
    font-weight: 700;
    font-size: 46px;
    letter-spacing: 1px;
  }
  .photo-band {
    position: absolute;
    top: 141px; left: 0; right: 0;
    height: 156px;
  }
  .photo {
    position: absolute;
    top: 0; height: 156px;
  }
  .photo-living {
    left: 0; width: 304px;
    border-radius: 0 16px 16px 0;
    background: linear-gradient(180deg, var(--photo-light) 0%, #d8d5cf 55%, var(--photo-mid) 80%, var(--photo-wood) 100%);
  }
  .photo-hall {
    left: 318px; width: 304px;
    border-radius: 16px 0 0 16px;
    background: linear-gradient(90deg, #d9d6d0 0%, #bdb8b0 40%, #6e6f72 62%, #b7bcc0 100%);
  }
  .affiliations {
    position: absolute;
    top: 318px; left: 103px;
    display: flex; align-items: center; gap: 22px;
  }
  .badge { background: rgba(255,255,255,0.85); border-radius: 3px; height: 26px; }
  .badge-a { width: 118px; }
  .badge-b { width: 134px; }
  .badge-c { width: 128px; }

  /* Back */
  .card-back {
    left: 276px; top: 608px;
    background: var(--card-white);
  }
  .back-photo {
    position: absolute;
    right: 0; top: 0;
    width: 310px; height: 375px;
    background: linear-gradient(180deg, #eeedea 0%, #e2e0db 40%, #d3d0ca 70%, #a99680 100%);
    -webkit-mask-image: linear-gradient(90deg, transparent 0%, #000 30%);
    mask-image: linear-gradient(90deg, transparent 0%, #000 30%);
  }
  .back-wordmark {
    position: absolute;
    left: 32px; top: 58px;
    color: var(--brand-blue);
    font-weight: 700;
    font-size: 40px;
    letter-spacing: 0.5px;
  }
  .holder-name {
    position: absolute;
    left: 32px; top: 172px;
    font-family: "Russo One", Arial, sans-serif;
    font-size: 24px;
    color: var(--brand-blue-deep);
    letter-spacing: 0.3px;
  }
  .holder-title {
    position: absolute;
    left: 32px; top: 203px;
    font-size: 16px;
    color: var(--ink);
  }
  .contact-list {
    position: absolute;
    left: 32px; top: 256px;
    list-style: none;
  }
  .contact-list li {
    display: flex; align-items: center;
    height: 24px;
    font-size: 16.5px;
    color: var(--ink);
  }
  .contact-list svg { width: 16px; height: 16px; margin-right: 16px; fill: var(--brand-blue-deep); }
  .contact-list .web-mid { color: var(--link-blue); }
  .mailing-address {
    position: absolute;
    left: 32px; top: 335px;
    font-size: 16.5px;
    color: var(--ink);
  }
</style>
</head>
<body>

<section class="card card-front" aria-label="Card front">
  <div class="front-wordmark">Bramwick Drywall</div>
  <div class="photo-band">
    <div class="photo photo-living" role="img" aria-label="Bright high-end living room with white sofas, fireplace and coffered ceiling"></div>
    <div class="photo photo-hall" role="img" aria-label="Luxury home entry hall opening into a modern living room"></div>
  </div>
  <div class="affiliations" aria-label="Trade association memberships">
    <div class="badge badge-a"></div>
    <div class="badge badge-b"></div>
    <div class="badge badge-c"></div>
  </div>
</section>

<section class="card card-back" aria-label="Card back">
  <div class="back-photo" role="img" aria-label="Elegant living room with chandelier, fireplace and white armchairs"></div>
  <div class="back-wordmark">Bramwick Drywall</div>
  <h1 class="holder-name">DALE WHITCOMB</h1>
  <p class="holder-title">Founder &amp; Owner</p>
  <ul class="contact-list">
    <li>
      <svg viewBox="0 0 16 16" aria-hidden="true"><path d="M2 6c0-2 2-3 6-3s6 1 6 3v1h-3V5.5H5V7H2z"/><rect x="3" y="8" width="10" height="6" rx="1"/></svg>
      555.214.0386
    </li>
    <li>
      <svg viewBox="0 0 16 16" aria-hidden="true"><path d="M1 3h14v10H1z M2.5 4.5 8 9l5.5-4.5" stroke="#fff" stroke-width="1.2"/></svg>
      Dale@BramwickDrywallServices.com
    </li>
    <li>
      <svg viewBox="0 0 16 16" aria-hidden="true"><circle cx="8" cy="8" r="7"/><path d="M1 8h14M8 1v14M3 4.5h10M3 11.5h10" stroke="#fff" stroke-width="1" fill="none"/><ellipse cx="8" cy="8" rx="3" ry="7" stroke="#fff" stroke-width="1" fill="none"/></svg>
      <span><span class="web-mid">BramwickDrywallServices</span>.com</span>
    </li>
  </ul>
  <p class="mailing-address">PO BOX 208 ASHFORD, TX 75501</p>
</section>

</body>
</html>
```